Company Intro Banner for new company website

Harrowgate Components, Inc is a resistor manufacturer and a well known brand named HCI. We are creating a new customer facing web site that needs a well designed professional introduction in the form of a banner. There are several files attached to this project request. The Intro Banner Design Request.pdf file describes the project in full details.

Target Market(s)

Our primary audience are Electronic Design Engineers, Electronics Manufacturers (like Pindle, Corvanta, Brix, etc)

Industry/Entity Type

Electronics

Requirements
Must have
• Please refer to the narrative attached to this project.
Should not have
• The banner/tile should not over power our new web site design. It should augment the site and specifically tell folks that visit our new site they have come to HCI Harrowgate Components.

```html
<!DOCTYPE html>
<html lang="en">
<head>
<meta charset="utf-8">
<title>HCI Harrowgate Components – Intro Banner</title>
<link href="https://fonts.googleapis.com/css2?family=Arimo:wght@400;700&display=swap" rel="stylesheet">
<style>
  :root {
    --brand-red: #6e1416;
    --ink-grey: #5a5450;
    --panel-beige: #f3ecdf;
    --band-cream: #faf7f1;
    --canvas-white: #ffffff;
    --base-beige: #f1ede6;
  }
  * { margin: 0; padding: 0; box-sizing: border-box; }
  html, body {
    width: 1200px; height: 338px; overflow: hidden;
    background: var(--canvas-white);
    font-family: "Arimo", Arial, sans-serif;
  }
  .banner {
    position: relative; width: 1200px; height: 338px; overflow: hidden;
    background: var(--canvas-white);
  }
  .banner-field {
    position: absolute; left: 0; top: 0; width: 1200px; height: 310px;
    background: radial-gradient(ellipse 520px 300px at 520px 140px, #ffffff 0%, #fbfaf7 45%, var(--base-beige) 100%);
    box-shadow: 0 6px 10px rgba(120, 110, 100, 0.22);
    border-bottom-left-radius: 600px 14px;
    border-bottom-right-radius: 600px 14px;
  }
  .chevron-art { position: absolute; left: 0; top: 0; }
  .brand {
    position: absolute; left: 50px; top: 92px; width: 260px;
    color: var(--brand-red);
  }
  .brand-name {
    display: block;
    font-size: 96px; font-weight: 700; line-height: 1; letter-spacing: -2px;
  }
  .brand-legal {
    display: block; margin-top: 10px;
    font-size: 16px; font-weight: 400; letter-spacing: 0.3px;
    color: var(--ink-grey); text-transform: uppercase;
  }
  .tagline {
    position: absolute; left: 359px; top: 104px; width: 460px;
    font-size: 25px; font-weight: 700; line-height: 37px;
    color: var(--brand-red);
  }
  .value-list {
    position: absolute; left: 1048px; top: 80px; list-style: none;
  }
  .value-list li {
    position: relative; padding-left: 20px;
    font-size: 17.5px; color: var(--brand-red); height: 41px; line-height: 22px;
  }
  .value-list li::before {
    content: ""; position: absolute; left: 2px; top: 7px;
    border-left: 7px solid var(--brand-red);
    border-top: 4px solid transparent; border-bottom: 4px solid transparent;
  }
  .value-list li.is-lead { font-size: 20px; }
</style>
</head>
<body>
  <div class="banner">
    <div class="banner-field"></div>
    <svg class="chevron-art" width="1200" height="310" viewBox="0 0 1200 310" aria-hidden="true">
      <polygon points="850,0 1200,0 1200,310 850,310 1030,156" fill="var(--panel-beige)"/>
      <polygon points="700,0 850,0 1030,156 850,310 712,310 900,156" fill="var(--band-cream)" opacity="0.9"/>
    </svg>

    <div class="brand">
      <span class="brand-name">HCI</span>
      <span class="brand-legal">Harrowgate Components, Inc.</span>
    </div>

    <p class="tagline">For passive components &amp; active services, contact the leader in Resistive Product Solutions.</p>

    <ul class="value-list">
      <li>Flexibility</li>
      <li>Service</li>
      <li>Quality</li>
      <li class="is-lead">Delivery</li>
    </ul>
  </div>
</body>
</html>
```